Canvasline Registry, LLC needs clean, modern business card design

Canvasline Registry is based in Honolulu. We offer fine arts collections management and documentation services for private and corporate art collectors. I would like to use my logo (attached). Card can be either single or double sided and either vertical or horizontal. My clients are businesses with art collections (banks, law firms, etc.) and wealthy individual collectors.

```html
<!DOCTYPE html>
<html lang="en">
<head>
<meta charset="utf-8">
<title>Canvasline Registry – Business Card</title>
<link href="https://fonts.googleapis.com/css2?family=Lato:wght@400;700&display=swap" rel="stylesheet">
<style>
  :root {
    --page-bg: #ecebe8;
    --card-dark: #58585a;
    --card-white: #ffffff;
    --card-white-shade: #eeeeee;
    --brand-blue: #29a8e0;
    --ink-grey: #4a4a4c;
    --text-light: #ffffff;
    --title-light: #d8f0fb;
  }
  * { margin: 0; padding: 0; box-sizing: border-box; }
  html, body {
    width: 1200px; height: 900px; overflow: hidden;
    background: var(--page-bg);
    font-family: "Lato", Arial, sans-serif;
  }
  .sheet {
    width: 1200px; height: 900px;
    display: flex; flex-direction: column;
    align-items: center; justify-content: center; gap: 60px;
  }
  .card {
    width: 560px; height: 320px; position: relative; overflow: hidden;
    box-shadow: 0 6px 18px rgba(0,0,0,0.18);
  }
  /* Back side */
  .card-back {
    background: var(--card-dark);
    display: flex; align-items: center; justify-content: center;
  }
  .card-back .brand-name {
    color: var(--text-light); font-weight: 700; font-size: 50px; letter-spacing: 0.5px;
  }
  /* Front side */
  .card-front { background: var(--card-white); }
  .front-top {
    position: absolute; left: 0; top: 0; width: 100%; height: 165px;
    background: radial-gradient(ellipse at 50% 30%, var(--card-white) 40%, var(--card-white-shade) 100%);
    display: flex; align-items: center; justify-content: center; gap: 14px;
    padding-bottom: 10px;
  }
  .front-top .brand-name {
    color: var(--ink-grey); font-weight: 700; font-size: 34px;
  }
  .brand-dot {
    width: 46px; height: 46px; border-radius: 50%;
    background: var(--brand-blue); opacity: 0.85;
  }
  .contact-band {
    position: absolute; left: 0; top: 165px; width: 100%; height: 115px;
    background: var(--brand-blue);
    display: flex; align-items: center; justify-content: center; gap: 26px;
  }
  .card-foot {
    position: absolute; left: 0; bottom: 0; width: 100%; height: 40px;
    background: var(--card-dark);
  }
  .person { text-align: right; color: var(--text-light); }
  .person-name { font-size: 22px; font-weight: 700; line-height: 1.1; }
  .person-title { font-size: 14px; color: var(--title-light); margin-bottom: 6px; }
  .person-address { font-size: 17px; line-height: 1.25; }
  .contact-list { list-style: none; color: var(--text-light); font-size: 14px; }
  .contact-list li { display: flex; align-items: center; gap: 8px; line-height: 1.6; }
  .contact-icon { width: 15px; height: 15px; flex: none; }
</style>
</head>
<body>
<main class="sheet">
  <section class="card card-back" aria-label="Card back">
    <span class="brand-name">Canvasline Registry</span>
  </section>

  <section class="card card-front" aria-label="Card front">
    <div class="front-top">
      <span class="brand-name">Canvasline Registry</span>
      <span class="brand-dot"></span>
    </div>
    <div class="contact-band">
      <div class="person">
        <p class="person-name">Maya Kealoha</p>
        <p class="person-title">Managing Director</p>
        <p class="person-address">1234, Kapiolani Blvd<br>Honolulu, 96814</p>
      </div>
      <ul class="contact-list">
        <li>
          <svg class="contact-icon" viewBox="0 0 16 16"><rect width="16" height="16" rx="2" fill="#fff"/><path d="M4 4h2l1 2-1.2 1a6 6 0 0 0 3.2 3.2L10 9l2 1v2a1 1 0 0 1-1 1A8 8 0 0 1 3 5a1 1 0 0 1 1-1z" fill="#29a8e0"/></svg>
          808-555-0142
        </li>
        <li>
          <svg class="contact-icon" viewBox="0 0 16 16"><rect width="16" height="16" rx="2" fill="#fff"/><rect x="4" y="3" width="8" height="4" fill="#29a8e0"/><rect x="3" y="7" width="10" height="4" rx="1" fill="#29a8e0"/><rect x="5" y="10" width="6" height="3" fill="#29a8e0"/></svg>
          808-555-0143
        </li>
        <li>
          <svg class="contact-icon" viewBox="0 0 16 16"><rect width="16" height="16" rx="2" fill="#fff"/><rect x="3" y="5" width="10" height="7" fill="#29a8e0"/><path d="M3 5l5 4 5-4" stroke="#fff" stroke-width="1" fill="none"/></svg>
          info@canvaslinereg.com
        </li>
        <li>
          <svg class="contact-icon" viewBox="0 0 16 16"><rect width="16" height="16" rx="2" fill="#fff"/><path d="M7 9l3-3M6 7l-1.5 1.5a2 2 0 0 0 3 3L9 10M10 9l1.5-1.5a2 2 0 0 0-3-3L7 6" stroke="#29a8e0" stroke-width="1.4" fill="none" stroke-linecap="round"/></svg>
          www.canvaslinereg.com
        </li>
      </ul>
    </div>
    <div class="card-foot"></div>
  </section>
</main>
</body>
</html>
```